letterhead design

We have a business card with logo, ink etc and want to develop letterhead that uses the elements of the business card logo.
Must haves...and they should be designed in, not just plopped in :)
Dr. Marla Quint
2817 W Birch Avenue
Fresno, CA 93728
559-555-0137 p
559-555-0182 f
info@ridgemoorchiropractic.com
www.ridgemoorchiropractic.com
www.friendpage.net/ridgemoorchiro
Updates

Rather than just have the logo on the page, is there someway to silkscreen it in the background to fill the page?

Reason: I was out of town for a week.

Industry/Entity Type

Business

Requirements
Nice to have
• I'd like the logo somehow silk screened in the background of the paper as well.

```html
<!DOCTYPE html>
<html lang="en">
<head>
<meta charset="utf-8">
<title>Ridgemoor Wellness Center – Letterhead</title>
<link href="https://fonts.googleapis.com/css2?family=Questrial&display=swap" rel="stylesheet">
<style>
  :root {
    --backdrop: #e6e6e6;
    --paper: #f4f4f4;
    --ink: #2b2b2b;
    --ink-soft: #555555;
    --rule: #6b6b6b;
    --ghost: #e7e7e7;
  }
  * { box-sizing: border-box; margin: 0; padding: 0; }
  html, body {
    width: 1200px;
    height: 936px;
    overflow: hidden;
    background: var(--backdrop);
    font-family: "Questrial", "Century Gothic", sans-serif;
    color: var(--ink);
  }
  .letterhead {
    position: absolute;
    left: 320px;
    top: 48px;
    width: 560px;
    height: 840px;
    background: var(--paper);
    box-shadow: 0 2px 6px rgba(0,0,0,0.08);
    overflow: hidden;
  }
  .brand-mark {
    position: absolute;
    left: 46px;
    top: 50px;
    display: flex;
    align-items: center;
    gap: 8px;
  }
  .brand-mark__dot {
    width: 14px;
    height: 14px;
    background: var(--ink);
  }
  .brand-mark__name {
    font-size: 20px;
    letter-spacing: 2px;
    color: var(--ink);
  }
  .background-name {
    position: absolute;
    left: 50%;
    top: 330px;
    transform: translateX(-50%);
    font-size: 104px;
    letter-spacing: 6px;
    color: var(--ghost);
    white-space: nowrap;
    user-select: none;
  }
  .contact-footer {
    position: absolute;
    left: 46px;
    right: 46px;
    bottom: 54px;
  }
  .contact-footer__rule {
    height: 1px;
    background: var(--rule);
  }
  .contact-footer__rows {
    padding: 9px 0;
    font-size: 9.5px;
    color: var(--ink-soft);
    line-height: 1.7;
  }
  .contact-footer__row {
    display: flex;
    align-items: center;
    gap: 10px;
  }
  .contact-item {
    display: inline-flex;
    align-items: center;
    gap: 4px;
  }
  .contact-item svg {
    width: 9px;
    height: 9px;
  }
</style>
</head>
<body>
  <main class="letterhead">
    <div class="brand-mark">
      <span class="brand-mark__dot"></span>
      <span class="brand-mark__name">RIDGEMOOR</span>
    </div>

    <div class="background-name" aria-hidden="true">RIDGEMOOR</div>

    <footer class="contact-footer">
      <div class="contact-footer__rule"></div>
      <div class="contact-footer__rows">
        <div class="contact-footer__row">
          <span class="contact-item">2817 W Birch Avenue, Fresno, CA 93728</span>
          <span class="contact-item">
            <svg viewBox="0 0 10 10"><circle cx="5" cy="5" r="5" fill="#555"/><path d="M3.2 2.6l1 .9-.5.8c.4.8 1 1.4 1.8 1.8l.8-.5.9 1-.7.8C4.6 7.1 2.9 5.4 2.6 3.3z" fill="#f4f4f4"/></svg>
            559-555-0137
          </span>
          <span class="contact-item">
            <svg viewBox="0 0 10 10"><circle cx="5" cy="5" r="5" fill="#555"/><rect x="2.6" y="3.6" width="4.8" height="3" fill="#f4f4f4"/><rect x="3.4" y="2.4" width="3.2" height="1.4" fill="#f4f4f4"/></svg>
            559-555-0182
          </span>
        </div>
        <div class="contact-footer__row">
          <span class="contact-item">
            <svg viewBox="0 0 10 10"><circle cx="5" cy="5" r="5" fill="#555"/><rect x="2.5" y="3.2" width="5" height="3.6" fill="#f4f4f4"/><path d="M2.5 3.2L5 5.2 7.5 3.2" stroke="#555" stroke-width="0.6" fill="none"/></svg>
            info@ridgemoorchiropractic.com
          </span>
          <span class="contact-item">
            <svg viewBox="0 0 10 10"><circle cx="5" cy="5" r="5" fill="#555"/><circle cx="5" cy="5" r="2.6" stroke="#f4f4f4" stroke-width="0.7" fill="none"/><path d="M2.4 5h5.2M5 2.4v5.2" stroke="#f4f4f4" stroke-width="0.6"/></svg>
            www.ridgemoorchiropractic.com
          </span>
        </div>
      </div>
      <div class="contact-footer__rule"></div>
    </footer>
  </main>
</body>
</html>
```